Business Cards Needed

Hi designers, I have a new logo that was created by one of the ArtMingle designers. I'd now like to use that logo to make business cards. The company is called VitaLumen Advisors and is a business consulting firm. I'd like the business cards to be horizontal, modern, and professional.
I'd like the following information to be on the business card:
1) Logo
2) my name - Marisa Kolvane
3) my title - Principal
4) name of business - VitaLumen Advisors
5) mobile - 508.372.9146
6) e-mail - marisa@vitalumenadvisors.example
I'm uploading a JPG file of the logo. I'm hoping this is the correct file format. Please let me know if you need another type of file. Thank you.
Look and feel
Each slider illustrates characteristics of the customer's brand and the style your logo design should communicate.

```html
<!DOCTYPE html>
<html lang="en">
<head>
<meta charset="utf-8">
<title>VitaLumen Advisors – Business Card</title>
<link href="https://fonts.googleapis.com/css2?family=Open+Sans:wght@400;600;700&display=swap" rel="stylesheet">
<style>
  :root {
    --stage: #e9eaec;
    --card-white: #ffffff;
    --brand-blue: #1b75bc;
    --brand-blue-dark: #1a4f95;
    --brand-green: #8cc63f;
    --text-grey: #4a4a4a;
    --divider: #2a6fba;
  }
  * { margin: 0; padding: 0; box-sizing: border-box; }
  html, body {
    width: 1200px; height: 800px; overflow: hidden;
    background: var(--stage);
    font-family: "Open Sans", Arial, sans-serif;
  }
  .canvas { position: relative; width: 1200px; height: 800px; }
  .card {
    position: absolute; top: 250px;
    width: 525px; height: 300px;
    border-radius: 22px; overflow: hidden;
    box-shadow: 0 10px 28px rgba(0,0,0,0.18);
  }
  .card--front { left: 45px; background: var(--card-white); }
  .card--back { left: 630px; background: var(--brand-blue); }

  .front-swoosh { position: absolute; inset: 0; }

  .brand-name {
    position: absolute;
    font-weight: 600;
    color: var(--brand-blue);
    white-space: nowrap;
  }
  .card--front .brand-name {
    left: 22px; top: 118px; font-size: 21px;
    display: flex; align-items: center; gap: 7px;
  }
  .brand-dot {
    width: 11px; height: 11px; border-radius: 50%;
    background: var(--brand-blue);
  }
  .card--back .brand-name {
    left: 0; right: 0; top: 124px; text-align: center;
    font-size: 40px; color: var(--brand-blue-dark);
  }

  .divider {
    position: absolute; left: 242px; top: 44px;
    width: 1.5px; height: 114px; background: var(--divider);
  }
  .contact { position: absolute; left: 256px; top: 40px; }
  .contact__name {
    font-weight: 700; font-size: 19px; color: var(--brand-blue);
    text-transform: uppercase; letter-spacing: 0.4px; line-height: 22px;
  }
  .contact__title {
    font-size: 13px; color: var(--text-grey); line-height: 18px; margin-bottom: 8px;
  }
  .contact__list { list-style: none; }
  .contact__item {
    display: flex; align-items: center; gap: 6px;
    font-size: 11px; color: var(--text-grey); line-height: 22px;
    white-space: nowrap;
  }
  .contact__icon { width: 11px; height: 11px; flex: none; }
</style>
</head>
<body>
<main class="canvas">

  <section class="card card--front" aria-label="Business card front">
    <svg class="front-swoosh" viewBox="0 0 525 300" aria-hidden="true">
      <path d="M150 300 C 300 260, 450 230, 525 165 L 525 300 Z" fill="var(--brand-green)"/>
      <path d="M178 300 C 318 266, 460 240, 525 184 L 525 300 Z" fill="var(--card-white)"/>
      <path d="M192 300 C 326 270, 465 246, 525 194 L 525 300 Z" fill="var(--brand-blue)"/>
    </svg>

    <div class="brand-name"><span class="brand-dot"></span>VitaLumen Advisors</div>

    <div class="divider"></div>

    <div class="contact">
      <div class="contact__name">Marisa Kolvane</div>
      <div class="contact__title">Principal</div>
      <ul class="contact__list">
        <li class="contact__item">
          <svg class="contact__icon" viewBox="0 0 12 12" aria-hidden="true"><circle cx="6" cy="6" r="6" fill="var(--brand-green)"/><path d="M3.5 3.2c.4-.4.9-.4 1.1 0l.6 1c.2.3.1.6-.2.8l-.3.2c.3.8.9 1.4 1.7 1.7l.2-.3c.2-.3.5-.4.8-.2l1 .6c.4.2.4.7 0 1.1-.6.6-1.5.7-2.4.2-1.3-.7-2.2-1.6-2.9-2.9-.4-.9-.3-1.8.4-2.2z" fill="#fff"/></svg>
          508.372.9146
        </li>
        <li class="contact__item">
          <svg class="contact__icon" viewBox="0 0 12 12" aria-hidden="true"><rect x="0" y="2" width="12" height="8" rx="1.5" fill="var(--brand-green)"/><path d="M1 3l5 3.5L11 3" stroke="#fff" stroke-width="1" fill="none"/></svg>
          marisa@vitalumenadvisors.example
        </li>
        <li class="contact__item">
          <svg class="contact__icon" viewBox="0 0 12 12" aria-hidden="true"><circle cx="6" cy="6" r="6" fill="var(--brand-green)"/><path d="M1 6h10M6 1c-2 2.5-2 7.5 0 10M6 1c2 2.5 2 7.5 0 10" stroke="#fff" stroke-width=".8" fill="none"/></svg>
          www.vitalumenadvisors.example
        </li>
      </ul>
    </div>
  </section>

  <section class="card card--back" aria-label="Business card back">
    <div class="brand-name">VitaLumen Advisors</div>
  </section>

</main>
</body>
</html>
```